Display ads - Med spa Velaxin promotion

Please create an ad creative for a promotional special for a med spa:
First-time customers who book a Velaxin appointment receive $50 off the Velaxin treatment

Please have an aspect of diversity in the ad (the company is black and woman-owned, so more than just white people in the ad creative

The company goes for "clean and tranquil" as part of their aesthetic

Attached here are the logo and picture of the homepage, and other images on the website, typical of the aesthetic of the company identity

you can find the website here for inspiration: thepetalroomspa.com

Please no "black and white" photography, full color only, thank you!

Target Market(s)

New Haven, Connecticut, wealthy individuals who want to look and feel younger, want great skin, and want to feel youthful

Industry/Entity Type

Medspa/beauty

Requirements
Must have
• Need 5 sizes that fit the following Medium rectangle: 300×250; Large rectangle: 300×600 ; 728x90, 300x50; 160x600
Nice to have
• Clean, refined, bright
Should not have
• black and white photos, cartoonish, or drawn items

```html
<!DOCTYPE html>
<html lang="en">
<head>
<meta charset="utf-8">
<title>The Petal Room – Velaxin Display Ads</title>
<link href="https://fonts.googleapis.com/css2?family=Raleway:wght@500;600&family=Montserrat:wght@500&display=swap" rel="stylesheet">
<style>
  :root{
    --board:#88e0a0;
    --sky:#00b9e3;
    --mint:#5bd69a;
    --navy:#0d2f5c;
    --marble:#f2f2f2;
    --label:#123a3a;
  }
  *{margin:0;padding:0;box-sizing:border-box}
  html,body{width:1200px;height:1200px;overflow:hidden;background:var(--board)}
  .board{position:relative;width:1200px;height:1200px;background:var(--board);font-family:"Raleway",sans-serif;font-variant-numeric:lining-nums}
  .ad{position:absolute;overflow:hidden;background:linear-gradient(160deg,#f7f7f7 0%,var(--marble) 50%,#ececec 100%);box-shadow:0 14px 22px rgba(0,40,20,.25)}
  .ad--tall{left:132px;top:61px;width:519px;height:1054px}
  .ad--skinny{left:766px;top:65px;width:279px;height:1040px}
  .ad svg.waves{position:absolute;inset:0;width:100%;height:100%;z-index:2}
  .photo{position:absolute;z-index:1;background:radial-gradient(ellipse closest-side at 50% 50%,#c48a66 0%,#9a6444 40%,#5a3828 72%,rgba(90,56,40,0) 100%)}
  .ad--tall .photo{left:120px;top:470px;width:460px;height:640px}
  .ad--skinny .photo{left:30px;top:595px;width:290px;height:470px}
  .foliage{position:absolute;border-radius:50%;background:radial-gradient(ellipse closest-side,rgba(150,210,215,.3),rgba(150,210,215,0))}
  .brand{position:absolute;left:0;right:0;z-index:3;display:flex;flex-direction:column;align-items:center}
  .brand__row{display:flex;align-items:center}
  .brand__dot{border:3px solid var(--sky);border-radius:50%}
  .brand__name{color:var(--navy);font-weight:500;line-height:1.12}
  .brand__tag{font-family:"Montserrat",sans-serif;font-weight:500;color:var(--navy)}
  .ad--tall .brand{top:106px}
  .ad--tall .brand__dot{width:52px;height:52px;margin-right:26px}
  .ad--tall .brand__name{font-size:21px}
  .ad--tall .brand__tag{font-size:11.5px;margin-top:12px}
  .ad--skinny .brand{top:181px}
  .ad--skinny .brand__dot{width:40px;height:40px;margin-right:18px;border-width:2.5px}
  .ad--skinny .brand__name{font-size:16px}
  .ad--skinny .brand__tag{font-size:9px;margin-top:10px}
  .offer{position:absolute;left:0;right:0;z-index:3;text-align:center;color:var(--navy);font-weight:500;letter-spacing:-.5px}
  .offer__lead{line-height:1.05}
  .offer__deal{color:var(--sky);border-top:2px solid var(--sky);border-bottom:2px solid var(--sky);margin:0 auto}
  .offer__deal small{font-size:.62em}
  .ad--tall .offer{top:232px}
  .ad--tall .offer__lead{font-size:32px}
  .ad--tall .offer__deal{width:354px;font-size:38px;line-height:48px;margin-top:14px}
  .ad--tall .offer__item{font-size:31px;margin-top:10px}
  .ad--skinny .offer{top:293px}
  .ad--skinny .offer__lead{font-size:20.5px;line-height:1.05}
  .ad--skinny .offer__deal{width:227px;font-size:25px;line-height:30px;margin-top:17px}
  .ad--skinny .offer__item{font-size:20px;margin-top:14px}
  .size-label{position:absolute;top:1135px;font-size:34px;color:var(--label);font-family:"Montserrat",sans-serif;font-weight:500;letter-spacing:1px;transform:translateX(-50%)}
</style>
</head>
<body>
<main class="board">

  <section class="ad ad--tall">
    <div class="foliage" style="left:360px;top:120px;width:200px;height:180px" role="img" aria-label="Faint leaf decoration"></div>
    <div class="foliage" style="left:-20px;top:460px;width:240px;height:180px" role="img" aria-label="Faint leaf decoration"></div>
    <div class="photo" role="img" aria-label="Smiling woman with curly hair"></div>
    <svg class="waves" viewBox="0 0 519 1054" preserveAspectRatio="none">
      <path d="M0 0H519V90C400 40 220 30 0 78Z" fill="var(--sky)"/>
      <path d="M0 78C200 40 400 45 519 112" fill="none" stroke="var(--mint)" stroke-width="3"/>
      <path d="M0 1054V930C60 1010 200 1030 330 1000C420 985 480 965 519 955V1054Z" fill="var(--sky)"/>
      <path d="M0 925C60 1000 200 1020 330 992C420 975 480 958 519 948" fill="none" stroke="var(--mint)" stroke-width="3"/>
    </svg>
    <div class="brand">
      <div class="brand__row"><span class="brand__dot"></span><div class="brand__name">The<br>Petal<br>Room</div></div>
      <div class="brand__tag">Your Skin Deserves Better</div>
    </div>
    <div class="offer">
      <div class="offer__lead">FIRST-TIME CUSTOMERS<br>WHO BOOK A<br>VELAXIN APPOINTMENT</div>
      <div class="offer__deal">RECEIVE $50 <small>OFF</small></div>
      <div class="offer__item">THE VELAXIN TREATMENT</div>
    </div>
  </section>

  <section class="ad ad--skinny">
    <div class="foliage" style="left:150px;top:100px;width:160px;height:140px" role="img" aria-label="Faint leaf decoration"></div>
    <div class="foliage" style="left:-10px;top:500px;width:200px;height:150px" role="img" aria-label="Faint leaf decoration"></div>
    <div class="photo" role="img" aria-label="Smiling woman with curly hair"></div>
    <svg class="waves" viewBox="0 0 279 1040" preserveAspectRatio="none">
      <path d="M0 0H279V62C200 58 100 60 0 84Z" fill="var(--sky)"/>
      <path d="M0 96C100 70 200 66 279 70" fill="none" stroke="var(--mint)" stroke-width="2.5"/>
      <path d="M0 1040V980C60 1005 160 1005 279 975V1040Z" fill="var(--sky)"/>
      <path d="M0 972C60 998 160 998 279 968" fill="none" stroke="var(--mint)" stroke-width="2.5"/>
    </svg>
    <div class="brand">
      <div class="brand__row"><span class="brand__dot"></span><div class="brand__name">The<br>Petal<br>Room</div></div>
      <div class="brand__tag">Your Skin Deserves Better</div>
    </div>
    <div class="offer">
      <div class="offer__lead">FIRST-TIME CUSTOMERS<br>WHO BOOK A VELAXIN<br>APPOINTMENT</div>
      <div class="offer__deal">RECEIVE $50 <small>OFF</small></div>
      <div class="offer__item">THE VELAXIN TREATMENT</div>
    </div>
  </section>

  <div class="size-label" style="left:391px">300×600</div>
  <div class="size-label" style="left:905px">160×600</div>
</main>
</body>
</html>
```